Timeshare sales and holiday rental business needs a brochure design

We need a brochure design for a holiday company based in Aberfoyle Scotland. We sell and rent out timeshare holidays worldwide. We are looking for a A4 sized leaflet which we can insert text in which explains our business. The leaflet would A4 but would be folded into a DL size. The design should incorporate exotic beach holidays but also holidays in the Scottish Highlands. The emphasis should be on quality holidays for a fraction of the price it would cost elsewhere.

Target Market(s)

Holiday Market

Industry/Entity Type

Business

```html
<!DOCTYPE html>
<html lang="en">
<head>
<meta charset="utf-8">
<title>Glenmora Holidays – Timeshare Leaflet</title>
<link rel="stylesheet" href="https://fonts.googleapis.com/css2?family=Open+Sans:wght@400;600;700&display=swap">
<style>
  :root {
    --page-bg: #e9eaec;
    --navy: #2a2d78;
    --navy-deep: #1f2260;
    --green: #1e7a3c;
    --sky-top: #3d5b92;
    --sky-mid: #8ea6c6;
    --mist: #dfe5ec;
    --white: #ffffff;
    --soft-white: #e6e9f6;
  }
  * { box-sizing: border-box; margin: 0; padding: 0; }
  html, body { width: 1200px; height: 800px; overflow: hidden; }
  body {
    background: var(--page-bg);
    font-family: "Open Sans", Arial, sans-serif;
    display: flex; align-items: center; justify-content: center;
  }
  .leaflet {
    position: relative;
    width: 540px; height: 764px;
    background: var(--white);
    box-shadow: 0 4px 18px rgba(0,0,0,.18);
    overflow: hidden;
  }
  .hero {
    position: absolute; inset: 0 0 auto 0; height: 384px;
  }
  .hero-scene {
    position: absolute; inset: 0;
    background: linear-gradient(180deg, var(--sky-top) 0%, #5f7eae 28%, var(--sky-mid) 52%, var(--mist) 78%, var(--white) 100%);
  }
  .hero-copy {
    position: relative; padding: 26px 30px 0 32px; color: var(--white);
  }
  .hero-title { font-size: 18px; font-weight: 700; line-height: 1.2; }
  .hero-tagline { font-size: 10.5px; font-weight: 700; margin-top: 2px; }
  .hero-text { font-size: 10px; line-height: 1.35; margin-top: 10px; }
  .photo {
    position: absolute; border: 5px solid var(--white);
    box-shadow: 0 3px 8px rgba(0,0,0,.35);
  }
  .photo-beach { left: 98px; top: 236px; width: 124px; height: 82px; transform: rotate(-4deg);
    background: linear-gradient(180deg, #3e8fd8 0%, #7cc3ec 45%, #1d9bc7 70%, #2f6fa6 100%); }
  .photo-highland { left: 254px; top: 222px; width: 166px; height: 90px; transform: rotate(-3deg);
    background: linear-gradient(180deg, #b9c5d8 0%, #d7d2cc 50%, #8a6e56 100%); }
  .photo-family { left: 178px; top: 262px; width: 166px; height: 108px; transform: rotate(-2deg);
    background: linear-gradient(180deg, #c9dcef 0%, #e8ddd0 55%, #b9c8da 100%); }
  .columns {
    position: absolute; top: 384px; left: 0; right: 0; bottom: 0;
    display: flex;
  }
  .services {
    width: 250px; background: linear-gradient(180deg, var(--navy) 0%, var(--navy-deep) 100%);
    color: var(--soft-white); padding: 18px 20px 0 30px;
  }
  .service + .service { margin-top: 18px; }
  .service-title { font-size: 14px; font-weight: 700; color: var(--white); margin-bottom: 2px; }
  .service-text { font-size: 11px; line-height: 1.4; }
  .offers { flex: 1; padding: 14px 22px 0 22px; color: var(--green); }
  .offers-title { font-size: 14px; font-weight: 700; margin-bottom: 10px; }
  .offer { margin-bottom: 10px; }
  .offer-title { font-size: 10px; font-weight: 700; line-height: 1.3; }
  .offer-text { font-size: 10px; line-height: 1.3; }
  .brand { display: flex; align-items: center; gap: 8px; margin: 12px 0 10px; }
  .brand-mark { width: 28px; height: 28px; border-radius: 50%; background: var(--navy); flex: none; }
  .brand-name { font-size: 16px; font-weight: 700; color: var(--navy); letter-spacing: .5px; white-space: nowrap; }
  .contact { font-size: 9px; line-height: 1.45; color: var(--navy); font-style: normal; }
  .contact strong { font-weight: 700; }
</style>
</head>
<body>
  <article class="leaflet">
    <header class="hero">
      <div class="hero-scene" role="img" aria-label="Snow-capped Highland mountains above a misty loch under a blue sky"></div>
      <div class="hero-copy">
        <h1 class="hero-title">Quality Timeshare Resales and<br>Timeshare Rentals Worldwide.</h1>
        <p class="hero-tagline">Timeshare means a lifetime of luxury holidays in resorts around the world.</p>
        <p class="hero-text">Once you become a Timeshare Owner your range of holiday options becomes enormous. You can use your timeshare resort as a home from home every year or exchange your weeks for a holiday at another timeshare resort, at one of over 4000 timeshare resorts world-wide that are available through the exchange facility.</p>
        <p class="hero-text">IF you are looking for a timeshare to exchange, look no further than Loch Ardair Highland Club, Perthshire, Scotland.</p>
      </div>
      <div class="photo photo-beach" role="img" aria-label="Tropical infinity pool with palm trees by the sea"></div>
      <div class="photo photo-highland" role="img" aria-label="Stag on a Highland hillside with snowy peaks"></div>
      <div class="photo photo-family" role="img" aria-label="Smiling family relaxing together on holiday"></div>
    </header>

    <section class="columns">
      <div class="services">
        <div class="service">
          <h2 class="service-title">Sell Timeshare</h2>
          <p class="service-text">Selling your timeshare property is simple with Glenmora Holidays. We have been selling for over 10 years and can manage the whole process for you.</p>
        </div>
        <div class="service">
          <h2 class="service-title">Buy Timeshare</h2>
          <p class="service-text">Buying your timeshare property is simple with Glenmora Holidays. We have been helping customers with this for over 10 years and can manage the whole process for you.</p>
        </div>
        <div class="service">
          <h2 class="service-title">Rent Timeshare</h2>
          <p class="service-text">Renting your timeshare property is simple with Glenmora Holidays. We have a wide range of vacation rental properties available.</p>
        </div>
      </div>

      <div class="offers">
        <h2 class="offers-title">Timeshare Offers</h2>
        <div class="offer">
          <h3 class="offer-title">Timeshare Resale Bargains List</h3>
          <p class="offer-text">Below is a very small selection of some of our best bargains picked from our vast inventory of Timeshare Resales. Please note that the costs also include the legal transfer fee.</p>
        </div>
        <div class="offer">
          <h3 class="offer-title">School Holiday Weeks - UK</h3>
          <p class="offer-text">Below is a small selection of school holiday weeks available in the UK, picked from our vast inventory of Timeshare Resales.</p>
        </div>
        <div class="offer">
          <h3 class="offer-title">School Holiday Weeks - Rest of the World</h3>
          <p class="offer-text">Below is a small selection of school holiday weeks available in Europe and Worldwide, picked from our vast inventory of Timeshare Resales.</p>
        </div>
        <div class="brand">
          <span class="brand-mark"></span>
          <span class="brand-name">GLENMORA HOLIDAYS</span>
        </div>
        <address class="contact">
          Birchlea, High Street, Kinlarig, Perthshire<br>
          Scotland, United Kingdom PH9 4QT<br>
          E-mail <strong>enquiries@glenmoraholidays.com</strong><br>
          Telephone <strong>+441796 555012</strong>
        </address>
      </div>
    </section>
  </article>
</body>
</html>
```